Electrical and Audio Visual Business Card Design

We need a business card design for our company called T.O.K.L.E (Tobin's Optic Kinetic & Lumen Engineering PtyLtd).
We provide Electrical Services as well as Audio Visual demands.
Services provided:
Electrical repairs
Additions
Extensions
Audio Visual solutions
Data
Smoke alarms
TV antennas
Automation
Updates

Also looking for a company logo. Uniforms are black if this helps.

Industry/Entity Type

Business

Contact Information for Business Card

T.O.K.L.E Pty Ltd
Martin Gollisby
58 Fenwick Rd,
Harlow Creek, 2471
mjgollisby@pelicanmail.com

Logo Text

T.O.K.L.E.

Requirements
Must have
• Please can we have a double sided card. Showing our services on the back. Can I also have the number 0451296847. Can we also change email address to mgollisby@tokle.net.au

```html
<!DOCTYPE html>
<html lang="en">
<head>
<meta charset="utf-8">
<title>T.O.K.L.E Business Card</title>
<link rel="stylesheet" href="https://fonts.googleapis.com/css2?family=Open+Sans:wght@400;600;700;800&display=swap">
<style>
  :root {
    --backdrop: #c98b4e;
    --card: #ffffff;
    --ink: #111111;
    --teal: #137b80;
    --white: #ffffff;
    --shadow: rgba(60, 30, 5, 0.35);
  }
  * { margin: 0; padding: 0; box-sizing: border-box; }
  html, body { width: 1200px; height: 1000px; overflow: hidden; }
  body {
    background: var(--backdrop);
    font-family: "Open Sans", Arial, sans-serif;
    color: var(--ink);
    position: relative;
  }
  .card {
    position: absolute;
    width: 750px;
    height: 440px;
    background: var(--card);
    box-shadow: 0 6px 18px var(--shadow);
  }
  .card-front { left: 30px; top: 25px; }
  .card-back { left: 30px; top: 515px; }

  /* Wordmark lockup */
  .lockup { position: absolute; }
  .lockup-name {
    display: flex;
    align-items: center;
    gap: 14px;
    font-weight: 700;
    line-height: 1;
  }
  .lockup-square { display: inline-block; }
  .lockup-rule { height: 3px; }
  .lockup-tagline { font-weight: 600; white-space: nowrap; }

  .card-front .lockup { left: 165px; top: 120px; }
  .card-front .lockup-name { font-size: 66px; color: var(--ink); }
  .card-front .lockup-square { width: 30px; height: 30px; background: var(--ink); }
  .card-front .lockup-rule { width: 330px; background: var(--teal); margin-top: 12px; }
  .card-front .lockup-tagline { font-size: 15px; margin-top: 4px; color: var(--ink); }

  .services {
    position: absolute;
    left: 0; right: 0; top: 300px;
    text-align: center;
    font-size: 19px;
    line-height: 38px;
  }

  /* Back */
  .holder { position: absolute; right: 40px; top: 90px; text-align: left; }
  .holder-name { font-size: 34px; font-weight: 800; line-height: 1.1; }
  .holder-rule { height: 3px; background: var(--teal); margin: 8px 0 6px; width: 330px; }
  .holder-company { font-size: 22px; color: var(--teal); letter-spacing: 0.32em; }

  .contact { position: absolute; display: flex; align-items: flex-start; gap: 20px; font-size: 20px; letter-spacing: 0.04em; }
  .contact svg { flex: none; fill: var(--teal); }
  .contact-address { left: 55px; top: 250px; line-height: 26px; }
  .contact-address address { font-style: normal; }
  .contact-phone { left: 385px; top: 310px; align-items: center; }
  .contact-email { left: 385px; top: 365px; align-items: center; }

  /* Logo variants */
  .variant { position: absolute; left: 835px; }
  .variant .lockup-name { font-size: 54px; }
  .variant .lockup-square { width: 24px; height: 24px; background: currentColor; }
  .variant .lockup-rule { width: 240px; margin-top: 6px; background: currentColor; }
  .variant .lockup-tagline { font-size: 11px; margin-top: 3px; }
  .variant-black { top: 180px; color: var(--ink); }
  .variant-white { top: 290px; color: var(--white); }
  .variant-teal { top: 405px; color: var(--teal); }
</style>
</head>
<body>

  <section class="card card-front" aria-label="Card front">
    <div class="lockup">
      <div class="lockup-name">T.O.K.L.E <span class="lockup-square"></span></div>
      <div class="lockup-rule"></div>
      <div class="lockup-tagline">Tobin's Optic Kinetic &amp; Lumen Engineering</div>
    </div>
    <p class="services">
      Electrical Repairs | Additions | Extensions | Audio Visual Solutions<br>
      Data | Smoke alarms | TV antennas | Automation
    </p>
  </section>

  <section class="card card-back" aria-label="Card back">
    <div class="holder">
      <div class="holder-name">Martin Gollisby</div>
      <div class="holder-rule"></div>
      <div class="holder-company">T.O.K.L.E Pty Ltd</div>
    </div>

    <div class="contact contact-address">
      <svg width="28" height="40" viewBox="0 0 28 40" aria-hidden="true">
        <path d="M14 0C6.3 0 0 6.3 0 14c0 10 14 26 14 26s14-16 14-26C28 6.3 21.7 0 14 0zm0 19a5 5 0 1 1 0-10 5 5 0 0 1 0 10z"/>
      </svg>
      <address>58 Fenwick Rd,<br>Harlow Creek,<br>2471</address>
    </div>

    <div class="contact contact-phone">
      <svg width="26" height="32" viewBox="0 0 26 32" aria-hidden="true">
        <path d="M6 1l5 7-3 3c1 4 4 8 8 11l3-3 6 5-3 5C12 28 2 16 1 6z"/>
      </svg>
      <span>0451-296-847</span>
    </div>

    <div class="contact contact-email">
      <svg width="32" height="24" viewBox="0 0 32 24" aria-hidden="true">
        <path d="M2 0h28a2 2 0 0 1 2 2v2L16 13 0 4V2a2 2 0 0 1 2-2zM0 7l16 9 16-9v15a2 2 0 0 1-2 2H2a2 2 0 0 1-2-2z"/>
      </svg>
      <span>mgollisby@tokle.net.au</span>
    </div>
  </section>

  <div class="lockup variant variant-black">
    <div class="lockup-name">T.O.K.L.E <span class="lockup-square"></span></div>
    <div class="lockup-rule"></div>
    <div class="lockup-tagline">Tobin's Optic Kinetic &amp; Lumen Engineering</div>
  </div>
  <div class="lockup variant variant-white">
    <div class="lockup-name">T.O.K.L.E <span class="lockup-square"></span></div>
    <div class="lockup-rule"></div>
    <div class="lockup-tagline">Tobin's Optic Kinetic &amp; Lumen Engineering</div>
  </div>
  <div class="lockup variant variant-teal">
    <div class="lockup-name">T.O.K.L.E <span class="lockup-square"></span></div>
    <div class="lockup-rule"></div>
    <div class="lockup-tagline">Tobin's Optic Kinetic &amp; Lumen Engineering</div>
  </div>

</body>
</html>
```